The Kindred Grove

I need a website design for my business in Ontario, Canada. I am a Bowen Therapist, Biofield Tuning Practitioner and Reiki Practitioner for People and animals. I want my website to convey a sense of connection, energy, and harmony which will align with my work in Bowen Therapy, Reiki, and Biofield Tuning Fork Therapy. I will be offering these services as well as downloadable audio files, subscriptions and online courses. I want the website to be simple, elegant and professional and most of all to be memorable. I treat animals as well so would like an aspect of this in the logo without looking cheesy. I want the logo to convey a sense of community for both online and in-person events. I want it to be appealing and approachable to those both familiar and unfamiliar with holistic modalities. I will be adding Nutrition, Iridology and herbal supports as services as well later into my journey.

Target Market(s)

Animal healing clients Pet Owners (older pets, stressed/anxious pets, recovering from surgery or injury) Holistic & Natural Pet Care Enthusiasts Working animals (show/agility competitors/breeders) Human healing clients – people dealing with musculoskeletal pain, mobility issues, chronic pain, stress & anxiety, PTSD, people already interested in holistic and alternative health practitioners, Athletes and performers looking to optimize function and recover, Courses People interested in learning for themselves and pets Audio files People interested in helping themselves and their pets

Industry/Entity Type

Holistic Wellness

Requirements
Should not have
• cluttered design, annoying pop ups, poor mobility experience

```html
<!DOCTYPE html>
<html lang="en">
<head>
<meta charset="utf-8">
<title>The Kindred Grove</title>
<link href="https://fonts.googleapis.com/css2?family=Poppins:ital,wght@0,300;0,400;0,500;0,600;0,700;1,400&display=swap" rel="stylesheet">
<style>
:root{
  --sage:#8fa39b;
  --sage-dark:#7d9189;
  --pink:#ebb5a9;
  --pink-soft:#f2cfc6;
  --sand:#ebe9e4;
  --taupe:#cfc3b5;
  --ink:#2f2f2f;
  --body:#4a4a4a;
  --muted:#a9b7ac;
  --white:#ffffff;
}
*{margin:0;padding:0;box-sizing:border-box}
html,body{width:1200px;height:4688px;overflow:hidden}
body{position:relative;font-family:'Poppins',sans-serif;color:var(--ink);background:var(--white)}
.abs{position:absolute}
.btn{position:absolute;display:flex;align-items:center;justify-content:center;background:var(--pink);color:var(--white);font-size:13px;font-weight:600;letter-spacing:.5px;text-transform:uppercase;border-radius:24px}
.h2{position:absolute;font-size:44px;font-weight:400;text-transform:uppercase;letter-spacing:1px;line-height:1.1;color:var(--ink)}
.para{position:absolute;font-size:14.5px;line-height:28px;color:var(--body)}
.band{position:absolute;left:0;width:1200px;background:var(--sand)}
.wave{position:absolute;left:0;width:1200px}

/* header */
.brand{left:73px;top:14px;display:flex;align-items:center;gap:12px}
.brand-dot{width:46px;height:46px;border-radius:50%;background:#f1a77f}
.brand-name{font-size:17px;font-weight:700;line-height:18px;color:#5a5a5a;text-transform:uppercase}
.phone{right:72px;top:26px;display:flex;align-items:center;gap:10px;font-size:22px;font-weight:600;color:#555}
.phone-ico{width:34px;height:34px;border-radius:50%;background:var(--sage);display:flex;align-items:center;justify-content:center}
.nav{left:0;top:84px;width:1200px;height:56px;background:var(--sage)}
.nav a{position:absolute;top:19px;font-size:13px;font-weight:600;color:var(--white);text-decoration:none;letter-spacing:.3px}
.nav a.active{color:#3a3a3a}
.book{position:absolute;right:0;top:0;width:300px;height:56px;background:var(--pink);clip-path:polygon(16px 0,100% 0,100% 100%,0 100%);color:var(--white);font-size:14px;font-weight:600;display:flex;align-items:center;padding-left:30px;letter-spacing:.3px}

/* hero */
.hero-photo{left:0;top:140px;width:1200px;height:670px;background:radial-gradient(ellipse at 78% 35%,#e8a76a 0%,#a66a3e 22%,#5a3a26 52%,#2e2018 100%)}
.hero-title{left:73px;top:368px;font-size:49px;font-weight:700;color:var(--white);letter-spacing:.5px}
.hero-sub{left:73px;top:428px;font-size:27px;font-weight:500;line-height:35px;color:var(--white)}
.dots{left:1127px;top:408px}
.dots span{display:block;width:11px;height:11px;border-radius:50%;background:var(--white);margin-bottom:12px}

/* welcome */
.welcome-photo{left:75px;top:893px;width:511px;height:422px;border-radius:0 110px 0 110px;background:linear-gradient(135deg,#6b5a7a 0%,#c7b2d8 45%,#efe6f0 60%,#8a78a8 100%)}

/* services */
.svc{position:absolute;top:1575px;width:250px;text-align:center}
.svc-ring{width:110px;height:110px;margin:0 auto;border-radius:50%;border:4px solid #d7d3cc;background:var(--white);display:flex;align-items:center;justify-content:center}
.svc-ring.on{border-color:var(--pink-soft)}
.svc h3{margin-top:20px;font-size:18px;font-weight:400;line-height:23px;text-transform:uppercase;color:var(--ink)}
.svc p{margin-top:8px;font-size:12.5px;line-height:24px;color:var(--body)}
.arrow{position:absolute;font-size:30px;color:#333;line-height:1}

/* about */
.portrait-back{left:690px;top:1994px;width:438px;height:438px;border-radius:50%;background:var(--sage)}
.portrait{left:704px;top:1986px;width:427px;height:427px;border-radius:50%;background:linear-gradient(160deg,#c8c3bd 0%,#8e8780 50%,#5b5a5d 100%)}

/* therapy cards */
.card{position:absolute;top:2609px;width:512px;height:532px;background:var(--white);border-radius:16px;overflow:hidden;text-align:center}
.card-photo{height:268px}
.card h3{margin-top:24px;font-size:35px;font-weight:400;text-transform:uppercase;color:var(--ink);letter-spacing:.5px}
.card p{margin:10px 22px 0;font-size:14.5px;line-height:24px;color:var(--body)}
.card .btn{position:relative;margin:22px auto 0;width:180px;height:48px}

/* testimonials */
.tcard{position:absolute;top:3398px;width:328px;height:270px;background:#f1f1ef;border-radius:14px;text-align:center;padding:24px 26px 0}
.tcard.lift{background:#f6f6f5;box-shadow:0 4px 14px rgba(0,0,0,.12)}
.quote{font-size:60px;font-weight:700;color:var(--pink);line-height:44px;height:40px;font-family:Georgia,serif}
.tcard p{margin-top:8px;font-size:13px;font-style:italic;line-height:24px;color:#444}
.tcard .who{margin-top:10px;font-size:13.5px;font-weight:600;color:var(--muted)}

/* contact */
.info{position:absolute;left:73px;display:flex;gap:16px}
.info-ico{width:40px;height:40px;border-radius:50%;border:1.5px solid #b9c4bd;display:flex;align-items:center;justify-content:center;margin-top:8px}
.info b{display:block;font-size:18px;font-weight:600;color:var(--ink)}
.info span{font-size:14px;color:var(--body)}
.social{left:73px;top:4216px;display:flex;gap:18px}
.social span{width:18px;height:18px;border-radius:50%;background:#333}
.form{left:614px;top:3848px;width:513px;height:413px;background:var(--taupe);border-radius:16px}
.form h2{position:absolute;left:24px;top:40px;font-size:42px;font-weight:400;text-transform:uppercase;color:var(--ink);letter-spacing:1px}
.field{position:absolute;background:var(--white);border-radius:22px;font-size:12px;color:#444;padding:12px 22px}
.submit{position:absolute;left:25px;top:334px;width:175px;height:43px;background:var(--sage);border-radius:22px;color:var(--white);font-size:13px;font-weight:600;display:flex;align-items:center;justify-content:center}

/* footer */
.foot-brand{left:78px;top:4460px;display:flex;align-items:center;gap:14px}
.foot-brand .brand-dot{width:62px;height:62px}
.foot-brand .brand-name{font-size:24px;line-height:25px}
.copy{left:77px;top:4562px;font-size:11px;line-height:22px;color:#333}
.fcol{position:absolute;top:4440px}
.fcol h4{font-size:16px;font-weight:600;text-transform:uppercase;color:var(--ink);margin-bottom:10px}
.fcol a{display:block;font-size:12.5px;line-height:31px;color:#444;text-decoration:none}
.fcol p{font-size:12.5px;line-height:22px;color:#444;width:250px}
.news-input{position:absolute;left:883px;top:4536px;width:242px;height:40px;border:1.5px solid #bbb;border-radius:20px;font-size:12.5px;padding:10px 20px;color:#333}
</style>
</head>
<body>

<!-- header -->
<div class="abs brand"><div class="brand-dot"></div><div class="brand-name">The<br>Kindred<br>Grove</div></div>
<div class="abs phone"><span class="phone-ico"><svg width="16" height="16" viewBox="0 0 24 24"><path d="M6.6 10.8a15 15 0 0 0 6.6 6.6l2.2-2.2a1 1 0 0 1 1-.25 11 11 0 0 0 3.6.6 1 1 0 0 1 1 1V20a1 1 0 0 1-1 1A17 17 0 0 1 3 4a1 1 0 0 1 1-1h3.5a1 1 0 0 1 1 1c0 1.25.2 2.45.6 3.6a1 1 0 0 1-.25 1z" fill="#fff"/></svg></span>+1 (555) 014-2290</div>
<nav class="abs nav">
  <a class="active" style="left:73px">HOME</a>
  <a style="left:155px">ABOUT</a>
  <a style="left:245px">SERVICES</a>
  <a style="left:354px">WHY US</a>
  <a style="left:450px">BLOG</a>
  <a style="left:528px">GALLERY</a>
  <a style="left:630px">TESTIMONIALS</a>
  <a style="left:776px">CONTACT US</a>
  <div class="book">BOOK AN APPOINTMENT</div>
</nav>

<!-- hero -->
<div class="abs hero-photo" role="img" aria-label="Photo of a woman relaxing during a gentle head treatment in a warm, softly lit room"></div>
<div class="abs hero-title">THE KINDRED GROVE</div>
<div class="abs hero-sub">Bowen Therapist, Biofield Tuning<br>Practitioner and Reiki Practitioner<br>for People and animals.</div>
<div class="btn" style="left:75px;top:559px;width:180px;height:46px">Read More</div>
<div class="abs dots"><span></span><span></span><span></span><span></span></div>
<svg class="wave" style="top:760px" height="70" viewBox="0 0 1200 70" preserveAspectRatio="none">
  <path d="M0 20 C250 55 450 0 700 25 S1050 45 1200 5 L1200 70 L0 70Z" fill="#8fa39b"/>
  <path d="M0 34 C250 66 470 12 720 36 S1050 52 1200 20 L1200 70 L0 70Z" fill="#ebb5a9"/>
  <path d="M0 40 C260 70 480 20 730 42 S1060 58 1200 28 L1200 70 L0 70Z" fill="#ffffff"/>
</svg>

<!-- welcome -->
<div class="abs welcome-photo" role="img" aria-label="Chakra meditation painting surrounded by healing crystals on lavender cloth"></div>
<div class="h2" style="left:615px;top:920px">Welcome to<br>The Kindred Grove</div>
<p class="para" style="left:615px;top:1030px;width:510px">Sed ut perspiciatis unde omnis iste natus error sit voluptatem accusantiumdoloremque laudantium, totam rem aperiam, eaque ipsa quae ab illo inventore veritatis et quasi architecto beatae vitae dicta sunt explicaboemo enim ipsam voluptatem quia voluptas sit aspernatur aut odit aut fugit, sed quia con sequuntur magni dolores eos.</p>
<div class="btn" style="left:615px;top:1231px;width:181px;height:47px">Read More</div>

<!-- services -->
<div class="band" style="top:1430px;height:460px"></div>
<svg class="wave" style="top:1390px" height="60" viewBox="0 0 1200 60" preserveAspectRatio="none">
  <path d="M0 8 C200 45 420 5 650 30 S1000 40 1200 12 L1200 60 L0 60Z" fill="#8fa39b"/>
  <path d="M0 22 C220 55 440 15 670 38 S1010 50 1200 24 L1200 60 L0 60Z" fill="#ebb5a9"/>
  <path d="M0 30 C230 60 450 22 680 44 S1020 56 1200 32 L1200 60 L0 60Z" fill="#ebe9e4"/>
</svg>
<div class="h2" style="left:0;width:1200px;text-align:center;top:1496px">Our Services</div>
<div class="arrow" style="left:40px;top:1672px">&#8249;</div>
<div class="arrow" style="left:1138px;top:1672px">&#8250;</div>
<div class="svc" style="left:70px">
  <div class="svc-ring"><svg width="52" height="52" viewBox="0 0 52 52" fill="none" stroke="#333" stroke-width="2"><rect x="8" y="32" width="36" height="6" rx="2"/><path d="M12 38v6M40 38v6"/><circle cx="18" cy="14" r="5"/><path d="M18 19l4 13M24 24h10"/></svg></div>
  <h3>Bowen Therapy</h3>
  <p>Sed ut perspiciatis unde omnis iste natus error sit volutatem accusa tium vitae dicta sunt</p>
</div>
<div class="svc" style="left:338px">
  <div class="svc-ring"><svg width="52" height="52" viewBox="0 0 52 52" fill="none" stroke="#333" stroke-width="2"><path d="M16 28V14a3 3 0 0 1 6 0v10V10a3 3 0 0 1 6 0v14V12a3 3 0 0 1 6 0v16l2-4a3 3 0 0 1 5 3l-5 11a11 11 0 0 1-20 0z"/><path d="M22 34c2 2 6 2 8 0"/></svg></div>
  <h3>Reiki</h3>
  <p>Sed ut perspiciatis unde omnis iste natus error sit volutatem accusa tium vitae dicta sunt</p>
</div>
<div class="svc" style="left:611px">
  <div class="svc-ring on"><svg width="52" height="52" viewBox="0 0 52 52" fill="none" stroke="#e08f9e" stroke-width="2"><path d="M21 8v14a5 5 0 0 0 10 0V8M26 27v18"/><path d="M14 14a10 10 0 0 0 0 14M10 10a16 16 0 0 0 0 22M38 14a10 10 0 0 1 0 14M42 10a16 16 0 0 1 0 22"/></svg></div>
  <h3>Biofield Tuning Fork<br>Therapy</h3>
  <p>Sed ut perspiciatis unde omnis iste natus error sit volutatem accusa tium vitae dicta sunt</p>
</div>
<div class="svc" style="left:878px">
  <div class="svc-ring"><svg width="52" height="52" viewBox="0 0 52 52" fill="none" stroke="#333" stroke-width="2"><rect x="12" y="8" width="24" height="18"/><path d="M16 14h16M16 19h10"/><rect x="8" y="26" width="36" height="18"/><path d="M30 40v-9l6-2v8"/><circle cx="28" cy="40" r="2"/></svg></div>
  <h3>Downloadable<br>Audio Files</h3>
  <p>Sed ut perspiciatis unde omnis iste natus error sit volutatem accusa tium vitae dicta sunt</p>
</div>
<svg class="wave" style="top:1872px" height="60" viewBox="0 0 1200 60" preserveAspectRatio="none">
  <path d="M0 0 L1200 0 L1200 40 C1000 10 800 55 560 30 S200 20 0 50Z" fill="#8fa39b"/>
  <path d="M0 0 L1200 0 L1200 30 C1000 2 800 45 560 22 S200 10 0 40Z" fill="#ebb5a9"/>
  <path d="M0 0 L1200 0 L1200 24 C1000 -2 800 38 560 16 S200 4 0 32Z" fill="#ebe9e4"/>
</svg>

<!-- about -->
<div class="h2" style="left:75px;top:2058px">About Me</div>
<p class="para" style="left:75px;top:2125px;width:570px">Sed ut perspiciatis unde omnis iste natus error sit voluptatem accusantiumdoloremque laudantium, totam rem aperiam, eaque ipsa quae ab illo inventore veritatis et quasi architecto beatae vitae dicta sunt explicaboemo enim ipsam voluptatem quia voluptas sit aspernatur aut odit aut fugit, sed quia con sequuntur magni dolores eos.</p>
<div class="btn" style="left:75px;top:2292px;width:180px;height:47px">Read More</div>
<div class="abs portrait-back"></div>
<div class="abs portrait" role="img" aria-label="Portrait of the practitioner, a smiling woman with long silver hair"></div>

<!-- therapy cards -->
<div class="band" style="top:2525px;height:735px"></div>
<svg class="wave" style="top:2478px" height="64" viewBox="0 0 1200 64" preserveAspectRatio="none">
  <path d="M0 10 C220 50 450 10 700 35 S1050 40 1200 8 L1200 64 L0 64Z" fill="#8fa39b"/>
  <path d="M0 24 C240 60 470 20 720 44 S1060 50 1200 20 L1200 64 L0 64Z" fill="#ebb5a9"/>
  <path d="M0 32 C250 64 480 28 730 50 S1070 58 1200 28 L1200 64 L0 64Z" fill="#ebe9e4"/>
</svg>
<div class="card" style="left:75px">
  <div class="card-photo" role="img" aria-label="Woman lying down during a tuning fork therapy session" style="background:linear-gradient(120deg,#6b3a2a 0%,#b05a3a 40%,#3f5f6c 75%,#2c3c48 100%)"></div>
  <h3>Therapy for People</h3>
  <p>Sed ut perspiciatis unde omnis iste natus error sit voluptatem accusantiumdoloremque laudantium, totam rem aperiam, eaque ipsa quae ab illo inventore veritatis et quasi architecto beatae vitae dicta sunt explicaboemo.</p>
  <div class="btn">Read More</div>
</div>
<div class="card" style="left:615px">
  <div class="card-photo" role="img" aria-label="Small dog resting while receiving a hands-on Reiki treatment" style="background:linear-gradient(120deg,#eae6e4 0%,#b7a7a0 40%,#4a3128 70%,#c8b6ae 100%)"></div>
  <h3>Therapy for Animals</h3>
  <p>Sed ut perspiciatis unde omnis iste natus error sit voluptatem accusantiumdoloremque laudantium, totam rem aperiam, eaque ipsa quae ab illo inventore veritatis et quasi architecto beatae vitae dicta sunt explicaboemo.</p>
  <div class="btn">Read More</div>
</div>

<!-- testimonials -->
<svg class="wave" style="top:3212px" height="66" viewBox="0 0 1200 66" preserveAspectRatio="none">
  <path d="M0 0 L1200 0 L1200 50 C1000 15 800 60 560 35 S200 25 0 58Z" fill="#8fa39b"/>
  <path d="M0 0 L1200 0 L1200 40 C1000 6 800 50 560 26 S200 14 0 48Z" fill="#ebb5a9"/>
  <path d="M0 0 L1200 0 L1200 32 C1000 0 800 42 560 18 S200 6 0 40Z" fill="#ebe9e4"/>
  <path d="M0 40 C200 6 560 18 560 18 S800 42 1200 32 L1200 66 L0 66Z" fill="#ffffff" opacity="0"/>
</svg>
<div class="band" style="top:3270px;height:0"></div>
<div class="h2" style="left:0;width:1200px;text-align:center;top:3316px">Client Testimonials</div>
<div class="arrow" style="left:42px;top:3518px">&#8249;</div>
<div class="arrow" style="left:1140px;top:3518px">&#8250;</div>
<div class="tcard" style="left:75px"><div class="quote">&#8221;</div><p>" Duis aute irure dolor in reprehenderit in voluptate velit esse cillum dolore eu fugiat nulla pariatur. Excepteur sint occaecat cupidatat non proident, sunt in culpa qui officia deserunt mollit anim id est laborum.."</p><div class="who">Leah, Guelph, ON</div></div>
<div class="tcard lift" style="left:436px"><div class="quote">&#8221;</div><p>" Duis aute irure dolor in reprehenderit in voluptate velit esse cillum dolore eu fugiat nulla pariatur. Excepteur sint occaecat cupidatat non proident, sunt in culpa qui officia deserunt mollit anim id est laborum.."</p><div class="who">Leah, Guelph, ON</div></div>
<div class="tcard" style="left:798px"><div class="quote">&#8221;</div><p>" Duis aute irure dolor in reprehenderit in voluptate velit esse cillum dolore eu fugiat nulla pariatur. Excepteur sint occaecat cupidatat non proident, sunt in culpa qui officia deserunt mollit anim id est laborum.."</p><div class="who">Leah, Guelph, ON</div></div>
<svg class="wave" style="top:3720px" height="70" viewBox="0 0 1200 70" preserveAspectRatio="none">
  <path d="M0 10 C250 55 470 5 720 30 S1050 50 1200 15 L1200 70 L0 70Z" fill="#8fa39b"/>
  <path d="M0 24 C260 66 480 16 730 40 S1060 60 1200 26 L1200 70 L0 70Z" fill="#ebb5a9"/>
  <path d="M0 32 C270 70 490 24 740 46 S1070 66 1200 34 L1200 70 L0 70Z" fill="#ebe9e4"/>
</svg>

<!-- contact -->
<div class="band" style="top:3788px;height:540px"></div>
<div class="h2" style="left:73px;top:3868px">Contact Info</div>
<p class="para" style="left:73px;top:3928px;width:510px;font-size:13.5px">Duis aute irure dolor in reprehenderit in voluptate velit esse cillum dolore eu fugiat nulla pariatur.</p>
<div class="info" style="top:4000px"><div class="info-ico"><svg width="14" height="14" viewBox="0 0 24 24"><path d="M12 2a7 7 0 0 0-7 7c0 5 7 13 7 13s7-8 7-13a7 7 0 0 0-7-7zm0 9.5A2.5 2.5 0 1 1 12 6.5a2.5 2.5 0 0 1 0 5z" fill="#8fa39b"/></svg></div><div><b>Address</b><span>48 Willow Lane, Guelph, Ontario N1H 2K3, Canada</span></div></div>
<div class="info" style="top:4066px"><div class="info-ico"><svg width="14" height="14" viewBox="0 0 24 24"><path d="M6.6 10.8a15 15 0 0 0 6.6 6.6l2.2-2.2a1 1 0 0 1 1-.25 11 11 0 0 0 3.6.6 1 1 0 0 1 1 1V20a1 1 0 0 1-1 1A17 17 0 0 1 3 4a1 1 0 0 1 1-1h3.5a1 1 0 0 1 1 1c0 1.25.2 2.45.6 3.6a1 1 0 0 1-.25 1z" fill="#8fa39b"/></svg></div><div><b>Phone</b><span>+1 (555) 014-2290</span></div></div>
<div class="info" style="top:4133px"><div class="info-ico"><svg width="14" height="14" viewBox="0 0 24 24"><path d="M3 6h18v12H3z" fill="#8fa39b"/><path d="M3 6l9 7 9-7" stroke="#fff" stroke-width="1.5" fill="none"/></svg></div><div><b>Email</b><span>hello@kindredgrove.example</span></div></div>
<div class="abs social" aria-label="Social media links"><span></span><span></span><span></span><span></span><span></span></div>

<div class="abs form">
  <h2>Get in Touch</h2>
  <div class="field" style="left:25px;top:96px;width:228px;height:42px">First Name</div>
  <div class="field" style="left:261px;top:96px;width:228px;height:42px">Last Name</div>
  <div class="field" style="left:25px;top:156px;width:228px;height:42px">Email Address</div>
  <div class="field" style="left:261px;top:156px;width:228px;height:42px">Subject</div>
  <div class="field" style="left:25px;top:216px;width:464px;height:100px">Message</div>
  <div class="submit">SUBMIT</div>
</div>

<!-- footer -->
<svg class="wave" style="top:4318px" height="72" viewBox="0 0 1200 72" preserveAspectRatio="none">
  <path d="M0 0 L1200 0 L1200 55 C1000 20 800 65 560 40 S200 28 0 62Z" fill="#8fa39b"/>
  <path d="M0 0 L1200 0 L1200 44 C1000 10 800 54 560 30 S200 16 0 52Z" fill="#ebb5a9"/>
  <path d="M0 0 L1200 0 L1200 36 C1000 2 800 46 560 22 S200 8 0 44Z" fill="#ebe9e4"/>
</svg>
<div class="abs foot-brand"><div class="brand-dot"></div><div class="brand-name">The<br>Kindred<br>Grove</div></div>
<div class="abs copy">© Copyright 2025 Company Name<br>All Rights Reserved.</div>
<div class="fcol" style="left:353px">
  <h4>Site Map</h4>
  <div style="display:flex;gap:46px">
    <div><a>Home</a><a>About</a><a>Services</a><a>Why Us</a><a>Blog</a></div>
    <div><a>Gallery</a><a>Testimonials</a><a>Contact Us</a></div>
  </div>
</div>
<div class="fcol" style="left:628px">
  <h4>Services</h4>
  <a>Bowen Therapy</a><a>Reiki</a><a>Biofield Tuning Fork Therapy</a><a>Downloadable audio files</a><a>Subscriptions</a><a>Online courses</a>
</div>
<div class="fcol" style="left:883px">
  <h4>Newsletter</h4>
  <p>Nemo enim ipsamluptatem quia voluptasspernatur utodit.</p>
</div>
<div class="news-input">Enter Email Address</div>
<div class="btn" style="left:883px;top:4589px;width:242px;height:42px">Submit</div>

</body>
</html>
```